"Harrow Crest Builders" is a residential building company and needs a new business card design and may re

We would like a redesign based on the existing logo, and would like to see a new font as well. We are bespoke home builders who build sustainable energy efficient homes.

Industry/Entity Type

Construction

Contact Information for Business Card

Business card size 40mm x 90mm

Colors

Designer to choose colors to be used in the design.

```html
<!DOCTYPE html>
<html lang="en">
<head>
<meta charset="utf-8">
<title>Harrow Crest Builders – Business Card</title>
<link href="https://fonts.googleapis.com/css2?family=Questrial&family=Mulish:ital,wght@1,800&family=Arimo:wght@700&display=swap" rel="stylesheet">
<style>
  :root {
    --backdrop: #3e1233;
    --paper: #eeeeee;
    --lime: #bbd037;
    --lime-deep: #adc132;
    --band: #dcdbdb;
    --ink: #111111;
  }
  html, body {
    margin: 0;
    width: 1200px;
    height: 1200px;
    overflow: hidden;
    background: var(--backdrop);
  }
  .stage {
    position: relative;
    width: 1200px;
    height: 1200px;
  }
  .card {
    position: absolute;
    top: 120px;
    width: 425px;
    height: 960px;
    background: var(--paper);
    overflow: hidden;
    box-shadow: 6px 8px 14px rgba(0,0,0,0.35);
    font-family: "Questrial", sans-serif;
    color: var(--ink);
  }
  .card--front { left: 142px; }
  .card--back { left: 633px; }
  .card__shapes {
    position: absolute;
    inset: 0;
  }

  /* Front */
  .front-wordmark {
    position: absolute;
    left: 212px;
    top: 400px;
    transform: translate(-50%, -50%) rotate(-90deg);
    white-space: nowrap;
    display: flex;
    align-items: center;
    gap: 22px;
  }
  .front-wordmark__mark {
    width: 38px;
    height: 38px;
    background: var(--lime);
  }
  .front-wordmark__name {
    font-size: 62px;
    line-height: 1.05;
    color: var(--ink);
  }

  /* Back */
  .back-wordmark {
    position: absolute;
    top: 34px;
    left: 0;
    right: 0;
    text-align: center;
    font-size: 24px;
    color: var(--ink);
  }
  .company-strip {
    position: absolute;
    left: 20px;
    top: 404px;
    transform-origin: 0 100%;
    transform: rotate(-21.4deg);
    font-family: "Arimo", sans-serif;
    font-weight: 700;
    font-size: 22px;
    white-space: nowrap;
    line-height: 1;
    margin-top: -22px;
  }
  .contact-person {
    position: absolute;
    right: 8px;
    top: 460px;
    text-align: right;
  }
  .contact-person__name {
    font-family: "Mulish", sans-serif;
    font-style: italic;
    font-weight: 800;
    font-size: 29px;
    line-height: 1.1;
  }
  .contact-person__phone {
    font-size: 22px;
    line-height: 1.2;
  }
  .contact-online {
    position: absolute;
    top: 614px;
    left: 0;
    right: 0;
    text-align: center;
    font-size: 21px;
    line-height: 38px;
    letter-spacing: 0.2px;
  }
  .contact-post {
    position: absolute;
    top: 762px;
    left: 0;
    right: 0;
    text-align: center;
    font-size: 23px;
    line-height: 29px;
  }
  .contact-registration {
    position: absolute;
    top: 852px;
    left: 0;
    right: 0;
    text-align: center;
    font-size: 17px;
  }
</style>
</head>
<body>
<main class="stage">

  <section class="card card--front" aria-label="Card front">
    <svg class="card__shapes" viewBox="0 0 425 960" aria-hidden="true">
      <polygon points="0,860 425,790 425,960 0,960" fill="var(--lime)"/>
      <polygon points="0,905 425,835 425,850 0,920" fill="var(--lime-deep)"/>
    </svg>
    <div class="front-wordmark">
      <span class="front-wordmark__mark"></span>
      <span class="front-wordmark__name">Harrow Crest<br>Builders</span>
    </div>
  </section>

  <section class="card card--back" aria-label="Card back">
    <svg class="card__shapes" viewBox="0 0 425 960" aria-hidden="true">
      <polygon points="0,0 425,0 425,163 0,330" fill="var(--lime)"/>
      <polygon points="0,300 425,133 425,148 0,315" fill="var(--lime-deep)"/>
      <polygon points="0,382 425,215 425,253 0,420" fill="var(--band)"/>
    </svg>

    <div class="back-wordmark">Harrow Crest Builders</div>
    <div class="company-strip">Harrow Crest Builders Pty Ltd</div>

    <div class="contact-person">
      <div class="contact-person__name">Daniel Marsh</div>
      <div class="contact-person__phone">0400 555 318</div>
    </div>

    <div class="contact-online">
      daniel@harrowcrestbuilders.com.au<br>
      www.harrowcrestbuilders.com.au
    </div>

    <div class="contact-post">
      PO Box 4172 Northgate<br>
      LPO Ashfield WA 6123
    </div>

    <div class="contact-registration">Registration 40518 ABN: 12 345 678 901</div>
  </section>

</main>
</body>
</html>
```